VoyaPoint

1. We need a four color business card
2. The Front of card needs to include our Logo, Slogan which is "Launching, Expanding & Optimizing Organizations, Individual Name, email, two phone numbers, email, skype address, website address
3. Back of card needs to include the following topics: Start Ups & Business Optimization,Product Acquisition, Destination Product Marketing & Representation,Marketing & Sales, Operations, Training/Education, Digital Marketing, Keynote Addresses/Public Speaking
3. Back of card can not be black as it needs to be a color that people can write on
Industry/Entity Type
Business

```html
<!DOCTYPE html>
<html lang="en">
<head>
<meta charset="utf-8">
<title>VoyaPoint Business Card</title>
<link rel="stylesheet" href="https://fonts.googleapis.com/css2?family=Open+Sans:wght@400;600;700&family=Alegreya+Sans+SC:wght@500&display=swap">
<style>
  :root {
    --page-bg: #e9e6e1;
    --card-white: #ffffff;
    --brand-blue: #1d6fb5;
    --brand-green: #8cbf3f;
    --deep-blue: #0f4f86;
    --mid-blue: #2a79b8;
    --light-blue: #6fb0e0;
    --text-grey: #5a5a5a;
    --rule-grey: #c9c9c9;
    --icon-blue: #1f5fa8;
  }
  * { margin: 0; padding: 0; box-sizing: border-box; }
  html, body { width: 1200px; height: 784px; overflow: hidden; }
  body {
    background: var(--page-bg);
    display: flex;
    align-items: center;
    justify-content: center;
    gap: 40px;
    font-family: "Open Sans", Arial, sans-serif;
  }
  .card {
    width: 540px;
    height: 309px;
    position: relative;
    overflow: hidden;
    box-shadow: 0 6px 18px rgba(0,0,0,.18);
  }

  /* Back side */
  .card-back {
    background: linear-gradient(135deg, var(--deep-blue) 0%, var(--mid-blue) 55%, var(--deep-blue) 100%);
    display: flex;
    align-items: center;
    justify-content: center;
  }
  .back-pattern {
    position: absolute;
    inset: 0;
    background: radial-gradient(ellipse at 15% 60%, rgba(111,176,224,.45) 0%, rgba(111,176,224,0) 55%),
                radial-gradient(ellipse at 90% 15%, rgba(111,176,224,.30) 0%, rgba(111,176,224,0) 45%);
  }
  .service-list {
    position: relative;
    list-style: none;
    text-align: center;
    font-family: "Alegreya Sans SC", "Open Sans", sans-serif;
    font-weight: 500;
    color: #ffffff;
    font-size: 15px;
    letter-spacing: 2.4px;
    line-height: 26px;
  }

  /* Front side */
  .card-front { background: var(--card-white); }
  .front-decoration {
    position: absolute;
    right: -30px;
    top: 30px;
    width: 200px;
    height: 230px;
    border-radius: 50%;
    background: radial-gradient(ellipse at 55% 25%, rgba(150,190,225,.35) 0%, rgba(240,200,170,.25) 45%, rgba(200,220,170,.22) 70%, rgba(255,255,255,0) 85%);
  }
  .brand {
    position: absolute;
    left: 34px;
    top: 52px;
    display: flex;
    align-items: center;
    gap: 12px;
  }
  .brand-dot {
    width: 44px;
    height: 44px;
    border-radius: 50%;
    background: var(--brand-green);
  }
  .brand-name {
    font-size: 40px;
    font-weight: 600;
    color: var(--brand-blue);
    letter-spacing: -0.5px;
  }
  .brand-rule {
    position: absolute;
    left: 92px;
    top: 108px;
    width: 270px;
    height: 1px;
    background: var(--rule-grey);
  }
  .slogan {
    position: absolute;
    left: 92px;
    top: 113px;
    font-size: 9px;
    letter-spacing: .6px;
    font-variant: small-caps;
    color: var(--text-grey);
  }
  .person {
    position: absolute;
    left: 34px;
    top: 150px;
  }
  .person-name {
    font-size: 18px;
    font-weight: 700;
    color: var(--brand-blue);
    line-height: 22px;
  }
  .person-title {
    font-size: 13px;
    color: var(--text-grey);
    margin-bottom: 8px;
  }
  .contact-list { list-style: none; }
  .contact-item {
    display: flex;
    align-items: center;
    gap: 6px;
    font-size: 14px;
    line-height: 20px;
    color: var(--text-grey);
  }
  .contact-icon { width: 14px; height: 14px; flex: none; }
</style>
</head>
<body>

  <section class="card card-back" aria-label="Card back">
    <div class="back-pattern" role="img" aria-label="Blue background with a receding pattern of soft light-blue dots"></div>
    <ul class="service-list">
      <li>Start Ups &amp; Business Optimization</li>
      <li>Product Acquisition</li>
      <li>Destination Product Marketing &amp; Representation</li>
      <li>Marketing &amp; Sales</li>
      <li>Operations</li>
      <li>Training/Education</li>
      <li>Digital Marketing</li>
      <li>Keynote Addresses/Public Speaking</li>
    </ul>
  </section>

  <section class="card card-front" aria-label="Card front">
    <div class="front-decoration" role="img" aria-label="Faint enlarged brand emblem decoration"></div>

    <div class="brand">
      <span class="brand-dot"></span>
      <span class="brand-name">VoyaPoint</span>
    </div>
    <div class="brand-rule"></div>
    <p class="slogan">Launching, Expanding &amp; Optimizing Organizations</p>

    <div class="person">
      <p class="person-name">Marin Hale</p>
      <p class="person-title">President</p>
      <ul class="contact-list">
        <li class="contact-item">
          <svg class="contact-icon" viewBox="0 0 24 24"><path fill="var(--icon-blue)" d="M6.6 10.8a15.1 15.1 0 0 0 6.6 6.6l2.2-2.2a1 1 0 0 1 1-.25 11.4 11.4 0 0 0 3.6.57 1 1 0 0 1 1 1V20a1 1 0 0 1-1 1A17 17 0 0 1 3 4a1 1 0 0 1 1-1h3.5a1 1 0 0 1 1 1c0 1.25.2 2.45.57 3.57a1 1 0 0 1-.25 1z"/></svg>
          (312)555-0142
        </li>
        <li class="contact-item">
          <svg class="contact-icon" viewBox="0 0 24 24"><path fill="var(--icon-blue)" d="M6.6 10.8a15.1 15.1 0 0 0 6.6 6.6l2.2-2.2a1 1 0 0 1 1-.25 11.4 11.4 0 0 0 3.6.57 1 1 0 0 1 1 1V20a1 1 0 0 1-1 1A17 17 0 0 1 3 4a1 1 0 0 1 1-1h3.5a1 1 0 0 1 1 1c0 1.25.2 2.45.57 3.57a1 1 0 0 1-.25 1z"/></svg>
          (312)555-0187
        </li>
        <li class="contact-item">
          <svg class="contact-icon" viewBox="0 0 24 24"><rect x="2" y="5" width="20" height="14" rx="2" fill="var(--icon-blue)"/><path d="M3 6l9 7 9-7" fill="none" stroke="#fff" stroke-width="1.8"/></svg>
          marin@voyapoint.com
        </li>
        <li class="contact-item">
          <svg class="contact-icon" viewBox="0 0 24 24"><circle cx="12" cy="12" r="10" fill="var(--icon-blue)"/><g fill="none" stroke="#fff" stroke-width="1.4"><ellipse cx="12" cy="12" rx="4.5" ry="10"/><path d="M2 12h20M4 7h16M4 17h16"/></g></svg>
          www.voyapoint
        </li>
        <li class="contact-item">
          <svg class="contact-icon" viewBox="0 0 24 24"><circle cx="12" cy="12" r="10" fill="var(--icon-blue)"/></svg>
          marin_voyapoint
        </li>
      </ul>
    </div>
  </section>

</body>
</html>
```